Redesign of business card for Silverbrook Mechanical

We are looking for a new design for our business cards for Silverbrook Mechanical. We are a plumbing & HVAC construction company, operating on the West Coast of Canada and USA. Logo attached.
Industry/Entity Type
Construction - Plumbing & HVAC
Contact Information for Business Card
Name, address, phone numbers, email, website address
Look and feel

```html
<!DOCTYPE html>
<html lang="en">
<head>
<meta charset="utf-8">
<title>Silverbrook Mechanical – Business Card</title>
<link rel="stylesheet" href="https://fonts.googleapis.com/css2?family=Montserrat:wght@400;500;700&display=swap">
<style>
  :root {
    --page-bg: #d9d4ce;
    --card-frost: #ebe6e0;
    --ink: #1c1c1c;
    --band: #141414;
    --band-text: #d8d2ca;
    --muted: #3a3a3a;
  }
  * { margin: 0; padding: 0; box-sizing: border-box; }
  html, body {
    width: 1200px;
    height: 1047px;
    overflow: hidden;
    background: var(--page-bg);
    font-family: "Montserrat", sans-serif;
  }
  .card {
    position: absolute;
    left: 100px;
    top: 250px;
    width: 1000px;
    height: 546px;
    border-radius: 24px;
    overflow: hidden;
    background: var(--card-frost);
    box-shadow: 0 10px 30px rgba(0,0,0,0.12);
  }
  .card__band {
    position: absolute;
    inset: 0;
    width: 1000px;
    height: 546px;
  }
  .brand {
    position: absolute;
    left: 40px;
    top: 40px;
    display: flex;
    align-items: center;
    gap: 20px;
  }
  .brand__mark {
    width: 66px;
    height: 66px;
    background: var(--ink);
  }
  .brand__name {
    font-weight: 700;
    font-size: 32px;
    line-height: 1.15;
    letter-spacing: 1px;
    text-transform: uppercase;
    color: var(--ink);
  }
  .person {
    position: absolute;
    right: 34px;
    top: 50px;
    padding-right: 26px;
    border-right: 10px solid var(--ink);
    text-align: right;
  }
  .person__name {
    font-weight: 700;
    font-size: 34px;
    letter-spacing: 1px;
    color: var(--ink);
    line-height: 1.1;
  }
  .person__title {
    font-weight: 500;
    font-size: 23px;
    color: var(--muted);
    margin-top: 6px;
  }
  .address {
    position: absolute;
    left: 40px;
    top: 290px;
    font-size: 27px;
    line-height: 39px;
    color: var(--muted);
  }
  .contacts {
    position: absolute;
    left: 40px;
    top: 402px;
    list-style: none;
  }
  .contacts__item {
    display: flex;
    align-items: center;
    gap: 12px;
    height: 39px;
    font-size: 25px;
    color: var(--band-text);
  }
  .contacts__icon {
    width: 20px;
    height: 20px;
    fill: var(--band-text);
  }
  .brand-small {
    position: absolute;
    left: 750px;
    top: 425px;
    display: flex;
    align-items: center;
    gap: 10px;
  }
  .brand-small__mark {
    width: 26px;
    height: 26px;
    background: var(--ink);
  }
  .brand-small__name {
    font-weight: 700;
    font-size: 19px;
    text-transform: uppercase;
    letter-spacing: 0.5px;
    color: var(--ink);
  }
</style>
</head>
<body>
  <div class="card">
    <svg class="card__band" viewBox="0 0 1000 546" aria-hidden="true">
      <path d="M0 406 H712 Q727 406 727 421 V476 Q727 491 742 491 H1000 V546 H0 Z" fill="var(--band)"/>
    </svg>

    <div class="brand">
      <div class="brand__mark"></div>
      <div class="brand__name">Silverbrook<br>Mechanical</div>
    </div>

    <div class="person">
      <div class="person__name">DANIEL HARTLEY</div>
      <div class="person__title">Managing Director</div>
    </div>

    <address class="address" style="font-style: normal;">
      Your address, City<br>
      State, Zip 1234
    </address>

    <ul class="contacts">
      <li class="contacts__item">
        <svg class="contacts__icon" viewBox="0 0 24 24"><path d="M6.6 10.8c1.4 2.8 3.8 5.1 6.6 6.6l2.2-2.2c.3-.3.7-.4 1-.2 1.1.4 2.3.6 3.6.6.6 0 1 .4 1 1V20c0 .6-.4 1-1 1C10.6 21 3 13.4 3 4c0-.6.4-1 1-1h3.5c.6 0 1 .4 1 1 0 1.3.2 2.5.6 3.6.1.3 0 .7-.2 1z"/></svg>
        <span>604 555 0192</span>
      </li>
      <li class="contacts__item">
        <svg class="contacts__icon" viewBox="0 0 24 24"><path d="M2 5h20v14H2z M4 7v.5l8 5 8-5V7z" fill-rule="evenodd"/></svg>
        <span>info@silverbrookmech.com</span>
      </li>
      <li class="contacts__item">
        <svg class="contacts__icon" viewBox="0 0 24 24"><circle cx="12" cy="12" r="10"/></svg>
        <span>www.silverbrookmech.com</span>
      </li>
    </ul>

    <div class="brand-small">
      <div class="brand-small__mark"></div>
      <div class="brand-small__name">Silverbrook Mechanical</div>
    </div>
  </div>
</body>
</html>
```